Sell the dream! Property investment proposal document

We are looking for a proposal document which outlines our vision for property development. The purpose of the document is to raise investment from investors - sell the dream!
Brief summary:
Tarrow Dwellings Developments, is an emerging New Zealand property investment company with a focus on providing unique property investment opportunities.
Our expertise and capabilities in architectural modular homes provide us with a remarkable advantage in tackling the development of properties that are typically considered challenging, remote, or uniquely positioned.
Our specialization in this niche sector of property development not only sets us apart from competitors, but also paves the way for lucrative investment opportunities in the New Zealand property market.
Feel free to use any images from www.tarrowdwellings.co.nz
Target Market(s)
investors for a unique property development opportunity
Industry/Entity Type
luxury property development in unique locations throughout New Zealand
Font styles to use
Colors
Designer to choose only greyscale colors for use in the design.
Look and feel

```html
<!DOCTYPE html>
<html lang="en">
<head>
<meta charset="utf-8">
<title>Tarrow Dwellings Developments – Investment Proposal Spread</title>
<link href="https://fonts.googleapis.com/css2?family=Poppins:wght@400;600&display=swap" rel="stylesheet">
<style>
  :root {
    --paper: #ffffff;
    --spread: #bababa;
    --spread-light: #c9c9c9;
    --ink: #111111;
    --mark: #8a8a8a;
    --fold: #ffffff;
  }
  * { box-sizing: border-box; margin: 0; padding: 0; }
  html, body { width: 1200px; height: 1200px; overflow: hidden; background: var(--paper); }
  .canvas { position: relative; width: 1200px; height: 1200px; font-family: "Poppins", sans-serif; color: var(--ink); }
  .artwork { position: absolute; inset: 0; }
  .column { position: absolute; font-size: 10.3px; line-height: 12.6px; text-align: justify; letter-spacing: 0.15px; }
  .column p { margin-bottom: 12.6px; }
  .column.tight p { margin-bottom: 0; }
  .column h2 { font-size: 13.6px; font-weight: 600; line-height: 16px; text-align: left; }
  .overview { left: 241px; top: 268px; width: 328px; }
  .origins { left: 241px; top: 645px; width: 328px; }
  .advantage { left: 632px; top: 224px; width: 511px; }
  .advantage h2 { margin-bottom: 10px; }
  .financial { left: 629px; top: 344px; width: 514px; }
  .financial h2 { margin-bottom: 10px; }
  .financial .market { padding-left: 1px; margin-top: 3px; }
</style>
</head>
<body>
<div class="canvas">
  <svg class="artwork" width="1200" height="1200" viewBox="0 0 1200 1200">
    <defs>
      <linearGradient id="interiorTone" x1="0" y1="0" x2="1" y2="1">
        <stop offset="0" stop-color="#d9d9d6"/><stop offset="0.5" stop-color="#a9a8a2"/><stop offset="1" stop-color="#cfcfcc"/>
      </linearGradient>
      <linearGradient id="coastTone" x1="0" y1="0" x2="0" y2="1">
        <stop offset="0" stop-color="#c9c3b5"/><stop offset="0.45" stop-color="#8a7e64"/><stop offset="1" stop-color="#4a4632"/>
      </linearGradient>
      <linearGradient id="viewTone" x1="0" y1="0" x2="0" y2="1">
        <stop offset="0" stop-color="#e6e6e4"/><stop offset="0.55" stop-color="#b9bcb0"/><stop offset="1" stop-color="#d8d4cc"/>
      </linearGradient>
      <linearGradient id="cliffTone" x1="0" y1="0" x2="0" y2="1">
        <stop offset="0" stop-color="#f1f1f1"/><stop offset="0.55" stop-color="#8d8d8a"/><stop offset="1" stop-color="#5c6a45"/>
      </linearGradient>
      <linearGradient id="seaTone" x1="0" y1="0" x2="0" y2="1">
        <stop offset="0" stop-color="#eef2f4"/><stop offset="0.3" stop-color="#9fc2d6"/><stop offset="0.6" stop-color="#3f7da0"/><stop offset="1" stop-color="#1a1a1e"/>
      </linearGradient>
    </defs>

    <!-- spread -->
    <rect x="24" y="190" width="1152" height="819" fill="var(--spread)"/>
    <polygon points="24,190 280,190 200,330 24,330" fill="var(--spread-light)" opacity="0.5"/>
    <polygon points="760,1009 820,880 1000,880 1000,1009" fill="var(--spread-light)" opacity="0.35"/>

    <!-- image areas -->
    <polygon role="img" aria-label="Photo: glass-walled interior overlooking dry hills" points="134,226 292,226 366,357 292,478 134,478 61,356" fill="url(#interiorTone)"/>
    <polygon points="290,238 440,238 585,428 440,478 290,478" fill="#d4d4d4" opacity="0.55"/>
    <polygon role="img" aria-label="Photo: low dark house on coastal farmland at dusk" points="96,464 202,464 239,542 202,620 96,620 60,542" fill="url(#coastTone)"/>
    <polygon role="img" aria-label="Photo: open living room framing a green valley and harbour" points="118,643 373,643 487,845 373,1000 118,1000 28,845" fill="url(#viewTone)"/>
    <polygon points="160,643 373,643 487,845 373,1000 240,1000 240,643" fill="#d0d0d0" opacity="0.45"/>

    <polygon role="img" aria-label="Photo: dark cantilevered house on a rocky hillside" points="683,578 798,578 851,674 798,770 683,770 632,674" fill="url(#cliffTone)"/>
    <polygon role="img" aria-label="Photo: lounge chairs before a wide ocean view" points="826,547 1112,547 1176,658 1176,845 1112,972 866,972 801,826 830,700" fill="url(#seaTone)"/>
    <polygon role="img" aria-label="Photo: bright interior with a valley and harbour view" points="677,781 807,781 851,876 801,974 677,974 632,876" fill="url(#viewTone)"/>

    <!-- fold line -->
    <line x1="601" y1="198" x2="601" y2="1009" stroke="var(--fold)" stroke-width="1.6" stroke-dasharray="6 7"/>

    <!-- crop marks -->
    <g stroke="var(--mark)" stroke-width="0.7">
      <line x1="31" y1="166" x2="31" y2="190"/><line x1="0" y1="198" x2="22" y2="198"/>
      <line x1="1169" y1="166" x2="1169" y2="190"/><line x1="1178" y1="198" x2="1200" y2="198"/>
      <line x1="31" y1="1011" x2="31" y2="1034"/><line x1="0" y1="1003" x2="22" y2="1003"/>
      <line x1="1169" y1="1011" x2="1169" y2="1034"/><line x1="1178" y1="1003" x2="1200" y2="1003"/>
    </g>
  </svg>

  <section class="column overview">
    <h2>Business Overview</h2>
    <p>Tarrow Dwellings Developments, is an emerging New zealand property investment company witha a focus on providing unique property investment opportunities.</p>
    <p>Our expertise ana capabilities in architechtural maodular homes provideus with a remarkable advantage in tacking the development of properties that are typically considered challenging, remote, our uniquely positioned.</p>
    <p>As a company, with 48 employees boasing a wealth of experience in handling complex architectural projects, making us well- equipped to navigate the intricacies and demands of such ventures.</p>
    <p>The advantage allows us to not only executes projects efficiently but also to deliver exceptional results within condensed time frames.</p>
    <p>By capiitalizing on our ability to develop difficult, remote, or one-of-a-kind properties swiftly and effectively, Tarrow Dwellings Developments offers investors a rare chance to engage in projects that promise exceptional profitability in the New Zealand property market.</p>
    <p>Our specialization in this niche sector or property development not only sets us apart from competitors, but also paves the way for lucrative investment opportunities in the New Zealanad property markrt.</p>
  </section>

  <section class="column origins">
    <h2>Business Origins</h2>
    <p>Tarrow Dwellings Developments was established with the goal of transforming the property investment market in New Zealand by introducing an innovative approch that centres on architectural modular designs and streamlined project time lines.</p>
    <p>Driven by our enthusiasm for architecture and real estate , we have expanded our successful business model to not only offer financial opportunities for investors but also to expand on our passion for high-end architectural design.</p>
    <p>With a wealth of experience accumulated over the past six years in the construction and the property market, we are pivoting to focus soley on our property development initiatives, presenting completed Tarrow projects to the market, in exclusive locations.</p>
    <p>These projects will boast high-quality standards, meticulous attention to deatail and landscaping, and creative design elements. By introducing completed Tarrow properties in to the market, we aim to reach a wider audience, catering to individuals who prefer ready-to-occupy homes, over engaging in the design construction process. This approach also simplifies the financing process for prospective buyers, as established properties are often preffered by financial lenders.</p>
  </section>

  <section class="column tight advantage">
    <h2>Competitive Advantage</h2>
    <p>Our competitive advantage lies in the uniqueness of our property investment opportunities.<br>Unlike traditional real estate companies, we focus on offering<br>properties that are not only profitable but also aesthetically pleasing and unique. By catering to the taste architecture lovers, we st ourselves apart from from the competition and atract a niche market of customers who appreciate the artistry and design of our projects. Additionaly, the streamlined and condenced timelines facilitatted our modular approach provide quicker returns on investment.</p>
  </section>

  <section class="column tight financial">
    <h2>Financial Summary</h2>
    <p>In terms of financial projections, with each development, we anticipate a profit of 10%-20% which will be project dependent.</p>
    <p>This growth is fueled by the increasing demand for unique property investments in New Zealand and our ability to deliver high-quality service to the market in a condensed time frame, with heavily controlled coasts.</p>
    <p>With s asolid business model and a delicated team, we are confident in our ability to achieve success and establish Tarrow Dwellings Investment as a trusted name in the industry.</p>
    <p class="market">New Zealand's property market has been experiencing steady growth over the years,making it an attractive destination for property investors. With its beautiful landscapes andstrong economy, New Zealand offers a diverse range of investment opportunities for bothlocal and international investors. The demand for quality properties in prime locationscontinues to rise, creating a favorable environment for property investment companies likeours that can lean on our modular benefits of being able to reach unique and remotelocations.</p>
  </section>
</div>
</body>
</html>
```